HIGH-END ANTI AGING START-UP NEEDS DOCUMENT/LETTERHEAD DESIGN!!!!

We are a high end anti-aging and health start-up catering to clients in Stamford and NYC. We just did a logo redesign and are now looking for a letter head design that we can use IN GOOGLE DOCS for marrowfieldcaregroup.example clients. We are REALLY EXCITED to see what you can show us!!!!!!!! We need something sophisticated and MODERN! Thanks so much!

Target Market(s)

High end, boutique medical clients. Our clientele is fairly high profile and we need a sleek, sophisticated letter head to put on all of our marketing materials and medical forms as well.

Industry/Entity Type

Medical

Font styles to use
Serif
Sans Serif

Colors
0255a3
ffffff
00a990
1b1b1b
919191

Requirements
Must have
• Must have the logo and "Marrowfield Care Group" written somewhere. Must have our URL www.marrowfieldcaregroup.example.
Nice to have
• office phone number (555) 374-9102
Should not have
• Colors outside of our logo colors + grey + black

```html
<!DOCTYPE html>
<html lang="en">
<head>
<meta charset="utf-8">
<title>Marrowfield Care Group — Letterhead</title>
<link rel="stylesheet" href="https://fonts.googleapis.com/css2?family=Libre+Baskerville:wght@700&family=Open+Sans:wght@400&display=swap">
<style>
  :root {
    --backdrop: #efefef;
    --paper: #ffffff;
    --brand-blue: #3f74e4;
    --brand-green: #009444;
    --rule-grey: #dcdcdc;
    --tint-green: #e4f2ea;
    --tint-blue: #e9effb;
    --footer-text: #ffffff;
  }
  * { box-sizing: border-box; margin: 0; padding: 0; }
  html, body {
    width: 1200px;
    height: 1200px;
    overflow: hidden;
    background: var(--backdrop);
  }
  .letterhead {
    position: absolute;
    left: 233px;
    top: 50px;
    width: 733px;
    height: 1100px;
    background: var(--paper);
    overflow: hidden;
  }
  .letterhead__header {
    position: absolute;
    left: 0;
    top: 0;
    width: 100%;
    height: 183px;
    border-bottom: 1px solid var(--rule-grey);
    display: flex;
    flex-direction: column;
    align-items: center;
  }
  .brand-mark {
    width: 84px;
    height: 84px;
    margin-top: 40px;
    border-radius: 50%;
    background: var(--brand-green);
  }
  .brand-name {
    margin-top: 14px;
    font-family: "Libre Baskerville", Georgia, serif;
    font-weight: 700;
    font-size: 17px;
    line-height: 1.2;
    letter-spacing: 0.04em;
    color: var(--brand-blue);
    text-transform: uppercase;
    text-align: center;
  }
  .backdrop-emblem {
    position: absolute;
    left: 38px;
    top: 256px;
    width: 658px;
    height: 658px;
    border-radius: 50%;
    background: linear-gradient(180deg, var(--tint-green) 0%, var(--tint-green) 40%, var(--tint-blue) 62%, rgba(233,239,251,0) 92%);
  }
  .letterhead__footer {
    position: absolute;
    left: 0;
    bottom: 0;
    width: 100%;
    height: 184px;
  }
  .footer-wave { position: absolute; inset: 0; width: 100%; height: 100%; }
  .footer-wave path { fill: var(--brand-green); }
  .contact {
    position: absolute;
    right: 56px;
    bottom: 37px;
    font-family: "Open Sans", Arial, sans-serif;
    font-size: 11.5px;
    line-height: 17px;
    color: var(--footer-text);
    text-align: right;
  }
</style>
</head>
<body>
  <main class="letterhead">
    <header class="letterhead__header">
      <div class="brand-mark" aria-hidden="true"></div>
      <h1 class="brand-name">Marrowfield<br>Care Group</h1>
    </header>

    <div class="backdrop-emblem" role="img" aria-label="Faint brand emblem watermark"></div>

    <footer class="letterhead__footer">
      <svg class="footer-wave" viewBox="0 0 733 184" preserveAspectRatio="none" aria-hidden="true">
        <path d="M0 111 C 260 128, 560 100, 733 0 L 733 184 L 0 184 Z"/>
      </svg>
      <address class="contact">
        (555) 374-9102<br>
        www.marrowfieldcaregroup.example
      </address>
    </footer>
  </main>
</body>
</html>
```